Business Card Design Project

Need a business card designed for a horse racing/gambling centered company.
Company name is BrightQuill.com.au
Company colours are similar to those in the logo.
Something clean and modern , designer given liberty to be creative.
Incorporate the logo is preferred.
Single or Double Sided fine
Must include :
Name
Mobile Number
Email Address
Reason: Apologies, I have been traveling unexpectedly with business and just need the extra two days to reply and give feedback before making a decision.
Industry/Entity Type
Business

```html
<!DOCTYPE html>
<html lang="en">
<head>
<meta charset="utf-8">
<title>BrightQuill Business Card</title>
<link href="https://fonts.googleapis.com/css2?family=Open+Sans:wght@300;400;600&display=swap" rel="stylesheet">
<style>
  :root {
    --teal: #1fa597;
    --teal-dark: #168a7e;
    --ink: #1c1c1c;
    --paper: #ffffff;
    --paper-tint: #f3f4f4;
    --backdrop: #e6e4e0;
    --edge-shadow: rgba(0, 0, 0, 0.18);
  }
  * { margin: 0; padding: 0; box-sizing: border-box; }
  html, body { width: 1200px; height: 900px; overflow: hidden; }
  body {
    background: var(--backdrop);
    font-family: "Open Sans", Arial, sans-serif;
    position: relative;
  }
  .card {
    position: absolute;
    left: 145px;
    top: 190px;
    width: 910px;
    height: 520px;
    background: var(--paper);
    box-shadow: 0 10px 30px rgba(0, 0, 0, 0.2);
    overflow: hidden;
  }
  .card-art { position: absolute; inset: 0; }
  .brand-mark {
    position: absolute;
    left: 44px;
    top: 44px;
    display: flex;
    align-items: center;
    gap: 14px;
  }
  .brand-dot {
    width: 78px;
    height: 78px;
    border-radius: 50%;
    background: var(--teal);
  }
  .brand-name {
    font-size: 20px;
    font-weight: 600;
    color: var(--teal);
  }
  .person { position: absolute; left: 50px; top: 150px; }
  .person-name {
    font-size: 36px;
    font-weight: 400;
    color: var(--teal);
    line-height: 1.1;
  }
  .person-role {
    font-size: 25px;
    font-weight: 600;
    color: var(--ink);
    line-height: 1.2;
  }
  .address {
    position: absolute;
    left: 50px;
    top: 255px;
    font-size: 22px;
    font-weight: 600;
    color: var(--ink);
    line-height: 1.3;
  }
  .contacts {
    position: absolute;
    left: 28px;
    top: 340px;
    list-style: none;
  }
  .contact-item {
    display: flex;
    align-items: center;
    gap: 16px;
    font-size: 22px;
    font-weight: 600;
    color: var(--ink);
    line-height: 1.45;
  }
  .contact-icon { width: 22px; height: 22px; flex: none; }
  .wordmark {
    position: absolute;
    left: 500px;
    top: 48px;
    font-size: 40px;
    font-weight: 300;
    color: var(--paper);
    letter-spacing: -0.5px;
  }
</style>
</head>
<body>
  <div class="card">
    <svg class="card-art" width="910" height="520" viewBox="0 0 910 520">
      <defs>
        <linearGradient id="track-scene" x1="0" y1="0" x2="1" y2="1">
          <stop offset="0" stop-color="#6b3a22"/>
          <stop offset="0.45" stop-color="#8a4a28"/>
          <stop offset="0.75" stop-color="#6f8f3e"/>
          <stop offset="1" stop-color="#8fb35a"/>
        </linearGradient>
        <linearGradient id="paper-tint" x1="0" y1="0" x2="1" y2="1">
          <stop offset="0" stop-color="#ffffff"/>
          <stop offset="1" stop-color="#f1f2f2"/>
        </linearGradient>
      </defs>
      <rect class="teal-band" x="0" y="0" width="910" height="165" fill="var(--teal)"/>
      <rect x="0" y="165" width="910" height="355" fill="url(#track-scene)" role="img" aria-label="Photo of racehorses and jockeys galloping on a turf track"/>
      <path d="M0 0 H400 C450 150 470 330 430 520 H0 Z" fill="var(--edge-shadow)" transform="translate(6 0)"/>
      <path class="info-panel" d="M0 0 H400 C450 150 470 330 430 520 H0 Z" fill="url(#paper-tint)"/>
    </svg>

    <div class="brand-mark">
      <span class="brand-dot"></span>
      <span class="brand-name">BrightQuill.com.au</span>
    </div>

    <div class="wordmark">BrightQuill.com.au</div>

    <div class="person">
      <div class="person-name">Liam Carter</div>
      <div class="person-role">Manager</div>
    </div>

    <div class="address">1207 /52 Harbour Lane<br>Sydney, NSW , 2000</div>

    <ul class="contacts">
      <li class="contact-item">
        <svg class="contact-icon" viewBox="0 0 22 22" aria-hidden="true">
          <rect width="22" height="22" rx="3" fill="var(--teal)"/>
          <path d="M6 5c1-1 2-1 2.5 0l1 2c.3.6 0 1.2-.5 1.6l-.6.5c.6 1.4 1.6 2.4 3 3l.5-.6c.4-.5 1-.8 1.6-.5l2 1c1 .5 1 1.5 0 2.5-1.5 1.5-4 1-6.5-1.5S4.5 6.5 6 5z" fill="#fff"/>
        </svg>
        <span>1300 555 012</span>
      </li>
      <li class="contact-item">
        <svg class="contact-icon" viewBox="0 0 22 22" aria-hidden="true">
          <rect width="22" height="22" rx="3" fill="var(--teal)"/>
          <rect x="4" y="6" width="14" height="10" rx="1" fill="#fff"/>
          <path d="M4.5 6.5 11 12l6.5-5.5" stroke="var(--teal)" stroke-width="1.5" fill="none"/>
        </svg>
        <span>info@brightquill.com.au</span>
      </li>
      <li class="contact-item">
        <svg class="contact-icon" viewBox="0 0 22 22" aria-hidden="true">
          <rect width="22" height="22" rx="3" fill="var(--teal)"/>
          <text x="11" y="16" text-anchor="middle" font-family="Open Sans, sans-serif" font-size="14" font-weight="600" fill="#fff">@</text>
        </svg>
        <span>www.brightquill.com.au</span>
      </li>
    </ul>
  </div>
</body>
</html>
```